Carpentry and Building Business Card

I'm looking for a business card that is minimalistic and that incorporates the theme of my Velmi logo.
On one side I'd like the VELMI logo with my details on the other side.
Double sided with curved edges

Target Market(s)

Construction / renovation
Adults

Industry/Entity Type

Tradesman

Contact Information for Business Card

Logo on one side, details on the other

Colors

Designer to choose only greyscale colors for use in the design.

Requirements
Must have
• Niko Barlettis
VELMI CONSTRUCT
Carpentry & Building Services
0412385726
Velmiconstruct@brindlemail.com
Lic No. 618243D
Nice to have
• Fb and insta icons. @velmiconstruct
Should not have
• No hammer or tool icons please.

No address line.

```html
<!DOCTYPE html>
<html lang="en">
<head>
<meta charset="utf-8">
<title>Velmi Construct Business Card</title>
<link href="https://fonts.googleapis.com/css2?family=Arimo:wght@400;700&display=swap" rel="stylesheet">
<style>
  :root {
    --bg: #d9d9d9;
    --grey-accent: #6f6f6f;
    --grey-deep: #2e2e2e;
    --grey-mid: #4a4a4a;
    --grey-light: #707070;
    --ink: #111111;
    --grey-rule: #9a9a9a;
    --white: #ffffff;
  }
  * { box-sizing: border-box; margin: 0; padding: 0; }
  html, body { width: 1200px; height: 900px; overflow: hidden; }
  body {
    background: var(--bg);
    font-family: "Arimo", Arial, sans-serif;
    position: relative;
  }
  .card {
    position: absolute;
    left: 250px;
    width: 700px;
    height: 400px;
    border-radius: 28px;
    overflow: hidden;
    box-shadow: 0 8px 24px rgba(0,0,0,0.18);
  }
  /* Front side */
  .card--front {
    top: 40px;
    background: radial-gradient(ellipse at 50% 45%, var(--grey-light) 0%, var(--grey-mid) 40%, var(--grey-deep) 90%);
    display: flex;
    align-items: center;
    justify-content: center;
  }
  .wordmark {
    display: flex;
    align-items: center;
    gap: 26px;
  }
  .wordmark__square {
    width: 56px;
    height: 56px;
    border: 3px solid currentColor;
  }
  .wordmark__name {
    font-weight: 400;
    letter-spacing: 0.32em;
    line-height: 1;
  }
  .card--front .wordmark { color: var(--white); }
  .card--front .wordmark__name { font-size: 52px; }

  /* Back side */
  .card--back {
    top: 460px;
    background: var(--white);
  }
  .card--back .wordmark {
    position: absolute;
    left: 130px;
    top: 56px;
    color: var(--ink);
  }
  .card--back .wordmark__square {
    border-color: var(--grey-accent);
    width: 70px;
    height: 70px;
  }
  .card--back .wordmark__name { font-size: 56px; }

  .identity {
    position: absolute;
    right: 390px;
    top: 176px;
    text-align: right;
    color: var(--ink);
  }
  .identity__name {
    font-size: 33px;
    font-weight: 700;
    color: var(--grey-accent);
    line-height: 1.05;
  }
  .identity__company,
  .identity__licence {
    font-size: 21px;
    line-height: 1.2;
  }
  .divider {
    position: absolute;
    left: 330px;
    top: 172px;
    width: 1.5px;
    height: 100px;
    background: var(--grey-rule);
  }
  .contacts {
    position: absolute;
    left: 352px;
    top: 170px;
    list-style: none;
    color: var(--ink);
    font-size: 19px;
  }
  .contacts li {
    display: flex;
    align-items: center;
    gap: 12px;
    height: 32px;
  }
  .contacts svg { width: 20px; height: 20px; flex: none; }
  .contacts .social-mark {
    width: 18px; height: 18px;
    background: var(--grey-accent);
    flex: none;
    margin-right: 2px;
  }
  .services-band {
    position: absolute;
    left: 0;
    top: 318px;
    width: 540px;
    height: 32px;
    background: var(--ink);
    color: var(--white);
    font-size: 20px;
    line-height: 32px;
    text-align: right;
    padding-right: 62px;
  }
  .accent-bar {
    position: absolute;
    right: 0;
    top: 290px;
    width: 80px;
    height: 40px;
    background: var(--grey-accent);
  }
</style>
</head>
<body>
  <section class="card card--front" aria-label="Card front">
    <div class="wordmark">
      <span class="wordmark__square"></span>
      <span class="wordmark__name">VELMI</span>
    </div>
  </section>

  <section class="card card--back" aria-label="Card back">
    <div class="wordmark">
      <span class="wordmark__square"></span>
      <span class="wordmark__name">VELMI</span>
    </div>

    <div class="identity">
      <p class="identity__name">Niko Barlettis</p>
      <p class="identity__company">VELMI CONSTRUCT</p>
      <p class="identity__licence">Lic No. 618243D</p>
    </div>

    <div class="divider"></div>

    <ul class="contacts">
      <li>
        <svg viewBox="0 0 24 24" aria-hidden="true"><path fill="#6f6f6f" d="M6.6 10.8a15.1 15.1 0 0 0 6.6 6.6l2.2-2.2c.3-.3.7-.4 1-.2 1.1.4 2.3.6 3.6.6.6 0 1 .4 1 1V20c0 .6-.4 1-1 1A17 17 0 0 1 3 4c0-.6.4-1 1-1h3.5c.6 0 1 .4 1 1 0 1.3.2 2.5.6 3.6.1.3 0 .7-.2 1z"/></svg>
        <span>0412385726</span>
      </li>
      <li>
        <svg viewBox="0 0 24 24" aria-hidden="true"><rect x="2" y="5" width="20" height="14" fill="#6f6f6f"/><path d="M2 5l10 8 10-8" fill="none" stroke="#fff" stroke-width="1.8"/></svg>
        <span>Velmiconstruct@brindlemail.com</span>
      </li>
      <li>
        <span class="social-mark"></span>
        <span>@velmiconstruct</span>
      </li>
    </ul>

    <div class="services-band">Carpentry &amp; Building Services</div>
    <div class="accent-bar"></div>
  </section>
</body>
</html>
```